Redesign of Brightvale.com website

Our website was initially developed 6+ years ago and has been maintained by several different designers. As a result, it is overly complex, inconsistent format/layout and the content is not well structured/easy to navigate

We need the site redeveloped with a more modern look and feel, simpler content structure and ability to implement new/improved tools, such as: Dynamic Forms, Sales Funnels, Landing Pages, improved metadata of our pages and posts, improved SEO/Page ranking, etc.

We currently use SalesForce CRM, Constant Contact for marketing automation and SmartSheet forms. We are investigating Zapier for workflow integration which could extend to our website.

Our current website is developed in WordPress, ideally we will stick with this platform, but we’re happy to consider other CMS' if strongly recommended. We may decide to remove/consolidate some of the pages and/or content as part of this re-design.

We don't want to rebrand (ie change corporate logo, colours scheme etc) as part of this website redevelopment and it is critical that we don't lose our current Page Ranking, SEO rankings, backlink benefits, etc as part of this redevelopment.

Sites we like the feel/design of are: plorvista.com, quindlefax.com and tovalip.com

Target Market(s)

Corporate, Enterprise and Government B2B clients.

Coding

Coded - Design and coding required

Number of Pages Required

5+ page

Font styles to use
Sans Serif

Colors
ffffff
ec1f27

Requirements
Must have
• Must retain the majority of content on our existing website (although we may re-write some of it as part of this redesign process).
Nice to have
• See above "Project Description"
Should not have

```html
<!DOCTYPE html>
<html lang="en">
<head>
<meta charset="utf-8">
<title>Brightvale – Business Continuity</title>
<link href="https://fonts.googleapis.com/css2?family=Open+Sans:ital,wght@0,400;0,600;0,700;1,400&family=Montserrat:wght@500;600;700&display=swap" rel="stylesheet">
<style>
:root{
  --red:#ec1f27;
  --red-dark:#c3151c;
  --ink:#222428;
  --text:#555a60;
  --muted:#8a8f95;
  --line:#e3e3e3;
  --paper:#ffffff;
  --grey-bg:#f2f2f2;
  --night:#14171c;
}
*{box-sizing:border-box;margin:0;padding:0}
html,body{width:1200px;height:3192px;overflow:hidden}
body{font-family:"Open Sans",Arial,sans-serif;color:var(--text);background:var(--paper);font-size:13px;position:relative}
h1,h2,h3,h4{font-family:"Montserrat",Arial,sans-serif;color:var(--ink)}

/* top bar */
.topbar{height:28px;border-bottom:1px solid var(--line);display:flex;align-items:center;padding:0 64px;font-size:11px;color:var(--muted);gap:28px}
.topbar span{display:flex;align-items:center;gap:6px}
.topbar svg{width:11px;height:11px;fill:var(--red)}

/* header */
.header{height:60px;display:flex;align-items:center;padding:0 64px}
.brand{display:flex;align-items:center;gap:8px;font-family:"Montserrat",sans-serif;font-weight:700;font-size:22px;color:var(--red)}
.brand i{width:16px;height:16px;border-radius:50%;background:var(--red);display:block}
.nav{margin-left:auto;display:flex;align-items:center;gap:2px}
.nav a{font-family:"Montserrat",sans-serif;font-size:12px;font-weight:600;color:var(--ink);text-decoration:none;padding:8px 10px}
.nav a.active{background:var(--red);color:#fff}
.nav .search{width:16px;height:16px;margin:0 14px 0 8px;stroke:var(--ink);fill:none;stroke-width:2}
.call{background:var(--red);color:#fff;display:flex;align-items:center;gap:8px;padding:6px 14px;font-family:"Montserrat",sans-serif}
.call small{display:block;font-size:9px;font-weight:500;opacity:.9}
.call b{font-size:15px}
.call svg{width:18px;height:18px;fill:#fff}

/* hero */
.hero{position:absolute;top:88px;left:0;width:1200px;height:472px;background:radial-gradient(ellipse at 40% 55%,#2f6fbf 0%,#173a75 35%,#0a1733 75%,#050b1a 100%)}
.hero-art{position:absolute;inset:0}
.hero-copy{position:absolute;left:600px;top:200px;color:#fff}
.hero-copy h1{color:#fff;font-size:26px;font-weight:700}
.hero-copy p{font-family:"Montserrat",sans-serif;font-size:20px;font-weight:600;margin-top:4px}
.hero-arrow{position:absolute;top:216px;width:34px;height:34px;stroke:#fff;stroke-width:3;fill:none}

/* services */
.services{position:absolute;top:580px;left:0;width:1200px;height:900px;background:var(--grey-bg)}
.col{position:absolute;width:330px}
.services-label{height:170px;background:linear-gradient(135deg,var(--red),#f25a2b);display:flex;align-items:center;padding-left:38px;box-shadow:0 6px 18px rgba(236,31,39,.25)}
.services-label h2{color:#fff;font-size:30px;line-height:1.1;font-weight:700;border-left:4px solid #fff;padding-left:14px}
.card{background:#fff;border-top:3px solid var(--red);padding:20px 26px 24px;box-shadow:0 3px 12px rgba(0,0,0,.06)}
.card h3{font-size:15px;font-weight:700;margin-bottom:12px}
.card ul{list-style:none}
.card li{font-size:11.5px;line-height:26px;border-bottom:1px dashed #ececec;padding-left:18px;position:relative}
.card li::before{content:"";position:absolute;left:2px;top:10px;width:7px;height:7px;border-radius:50%;border:2px solid var(--red)}
.btn{display:block;width:120px;margin:18px auto 0;background:var(--red);color:#fff;text-align:center;font-size:11px;font-weight:600;padding:8px 0}

/* safety band */
.safety{position:absolute;top:1512px;left:0;width:1200px;height:338px;background:linear-gradient(100deg,#2a1a12 0%,#6b3a1c 30%,#3a2a26 55%,#1b1c22 100%)}
.safety-copy{position:absolute;left:130px;top:100px}
.safety-copy h2{color:#fff;font-size:38px;line-height:1.18;font-weight:600}
.safety-copy h2::after{content:"";display:block;width:70px;height:4px;background:var(--red);margin-top:14px}
.safety-box{position:absolute;left:490px;top:30px;width:580px;height:278px;border:2px solid var(--red);background:rgba(236,31,39,.22);padding:20px 24px;color:#f0e6e0}
.safety-box h3{color:#fff;font-size:17px;margin-bottom:10px}
.safety-box p{font-size:11px;line-height:17px;margin-bottom:9px}

/* news */
.news{position:absolute;top:1850px;left:0;width:1200px;height:980px}
.news-head{position:absolute;left:128px;top:48px;width:1032px;display:flex;align-items:flex-end}
.news-head h2{font-size:30px;font-weight:700}
.news-head h2 span{color:var(--red)}
.tabs{margin-left:auto;display:flex;gap:26px;font-size:12px;font-weight:600;color:var(--ink)}
.tabs a{padding-bottom:6px}
.tabs .on{color:var(--red);border-bottom:2px solid var(--red)}
.news-rule{position:absolute;left:128px;top:106px;width:1032px;height:1px;background:var(--line)}
.post{position:absolute;background:#fff;box-shadow:0 3px 14px rgba(0,0,0,.08)}
.post .ph{height:var(--h)}
.post .body{padding:16px 20px}
.post h4{font-size:14px;line-height:19px}
.post .meta{font-size:10px;color:var(--red);margin:6px 0 8px}
.post p{font-size:11px;line-height:17px}
.news .btn{position:absolute;left:540px;top:880px;margin:0}

/* testimonials */
.testi{position:absolute;top:2848px;left:0;width:1200px;height:232px;background:linear-gradient(90deg,#2a2c30,#3a3c41)}
.testi-label{position:absolute;left:0;top:0;width:470px;height:232px;background:linear-gradient(120deg,var(--red-dark),var(--red) 60%,#f46a3a);display:flex;align-items:center;padding-left:128px}
.testi-label h2{color:#fff;font-size:34px;line-height:1.15;font-weight:500}
.avatar{position:absolute;left:520px;top:70px;width:74px;height:74px;border-radius:50%;background:linear-gradient(#b08d74,#6e5548);border:3px solid #fff}
.quote{position:absolute;left:620px;top:62px;width:520px;color:#e6e6e6;font-size:12px;line-height:19px;font-style:italic}
.quote b{display:block;font-style:normal;color:var(--red);font-size:11px;margin-top:8px}
.dots{position:absolute;left:820px;top:196px;display:flex;gap:8px}
.dots i{width:8px;height:8px;border-radius:50%;background:#777}
.dots i.on{background:var(--red)}

/* footer */
.footer{position:absolute;top:3080px;left:0;width:1200px;height:112px;background:var(--night);color:#aaa;padding:30px 128px}
.footer .brand{font-size:20px}
.footer small{display:block;font-size:10px;margin-top:8px;color:#888}
.footer-links{position:absolute;right:128px;top:38px;display:flex;gap:26px;font-size:11px;color:#ddd}
</style>
</head>
<body>

<div class="topbar">
  <span><svg viewBox="0 0 24 24"><path d="M2 5h20v14H2z M2 5l10 8 10-8" /></svg>info@brightvale.com.au</span>
  <span><svg viewBox="0 0 24 24"><path d="M12 2a7 7 0 0 0-7 7c0 5 7 13 7 13s7-8 7-13a7 7 0 0 0-7-7zm0 9.5A2.5 2.5 0 1 1 12 6.5a2.5 2.5 0 0 1 0 5z"/></svg>Level 8, Harbour Court, 44 Wattle Lane, Sydney NSW 2000 Australia</span>
</div>

<header class="header">
  <div class="brand"><i></i>Brightvale</div>
  <nav class="nav">
    <a class="active">HOME</a><a>SERVICES</a><a>ABOUT</a><a>CLIENTS</a><a>RESOURCES</a><a>BLOG</a><a>CONTACT</a>
    <svg class="search" viewBox="0 0 24 24"><circle cx="10" cy="10" r="7"/><path d="M15 15l7 7"/></svg>
    <div class="call"><svg viewBox="0 0 24 24"><path d="M6.6 10.8a15 15 0 0 0 6.6 6.6l2.2-2.2c.3-.3.7-.4 1-.2 1.1.4 2.3.6 3.6.6.6 0 1 .4 1 1V20c0 .6-.4 1-1 1A17 17 0 0 1 3 4c0-.6.4-1 1-1h3.5c.6 0 1 .4 1 1 0 1.3.2 2.5.6 3.6.1.3 0 .7-.2 1z"/></svg><div><small>CALL US</small><b>1300 BV PLAN</b></div></div>
  </nav>
</header>

<section class="hero">
  <div class="hero-art" role="img" aria-label="Photo of hands holding a tablet projecting a glowing city of data"></div>
  <svg class="hero-arrow" style="left:30px" viewBox="0 0 24 24"><path d="M15 4l-8 8 8 8"/></svg>
  <svg class="hero-arrow" style="right:30px" viewBox="0 0 24 24"><path d="M9 4l8 8-8 8"/></svg>
  <div class="hero-copy">
    <h1>Business Continuity</h1>
    <p>How Robust is Your Continuity Framework?</p>
  </div>
</section>

<section class="services">
  <div class="col" style="left:128px;top:28px">
    <div class="services-label"><h2>OUR<br>SERVICES</h2></div>
  </div>
  <div class="col" style="left:128px;top:218px">
    <div class="card">
      <h3>Resilience &amp; Continuity</h3>
      <ul>
        <li>Business Continuity Management</li><li>Disaster Recovery Planning</li><li>Crisis Management</li>
        <li>Emergency Management Planning</li><li>Workplace Health &amp; Safety</li><li>Pandemic Response Planning</li>
        <li>Risk Management</li><li>Strategy Development</li><li>Policy, Plans &amp; Procedures</li>
        <li>Plan Testing and Exercising</li><li>Maintenance, Governance &amp; Compliance</li>
        <li>Outsourcing &amp; Managed Services</li><li>Training Services</li><li>Backup &amp; Archiving Services</li>
      </ul>
      <span class="btn">Learn More</span>
    </div>
  </div>

  <div class="col" style="left:479px;top:28px">
    <div class="card">
      <h3>Software Solutions</h3>
      <ul><li>BC Planning Software</li><li>Crisis Software</li><li>GRC Software</li><li>SaaS BI</li></ul>
      <span class="btn">Learn More</span>
    </div>
  </div>
  <div class="col" style="left:479px;top:328px">
    <div class="card">
      <h3>IT Services &amp; Solutions</h3>
      <ul>
        <li>IT Disaster Recovery Planning</li><li>Software</li><li>Cloud Infrastructure</li><li>Application</li>
        <li>Solution Design &amp; Implementation</li><li>IT Service Management</li><li>IT Strategy &amp; Policy</li>
        <li>IT Sourcing</li><li>Vendor Management</li><li>Technology Architecture</li><li>Business Analysis</li>
        <li>Project Management</li><li>Technical Writing</li>
      </ul>
      <span class="btn">Learn More</span>
    </div>
  </div>

  <div class="col" style="left:830px;top:28px">
    <div class="card">
      <h3>Security Management</h3>
      <ul>
        <li>Information Security Policy</li><li>Security Management System</li><li>Cyber Security Awareness</li>
        <li>Security Review and Assessment</li><li>Security Audit Management</li><li>Vulnerability Identification</li>
        <li>Penetration Testing</li><li>Network Traffic Analysis</li>
      </ul>
      <span class="btn">Learn More</span>
    </div>
  </div>
  <div class="col" style="left:830px;top:448px">
    <div class="card">
      <h3>Data Management</h3>
      <ul>
        <li>Data Management Strategy</li><li>Data Management Documentation</li><li>Data Management Policy</li>
        <li>Data Management Planning</li><li>Awareness</li>
      </ul>
      <span class="btn">Learn More</span>
    </div>
  </div>
</section>

<section class="safety" role="img" aria-label="Aerial night photo of a city with glowing network lines">
  <div class="safety-copy"><h2>How To Ensure<br>Your Business Is<br>100% Safe</h2></div>
  <div class="safety-box">
    <h3>Your business is only as strong as its weakest link.</h3>
    <p>For over two decades we have helped organisations build resilience into every layer of their operations, from people and premises to technology and suppliers, so they can keep serving customers.</p>
    <p>Our consultants combine practical experience with proven frameworks to identify risk, plan responses and test recovery capability before a disruption ever occurs in your business.</p>
    <p>We work with corporate, enterprise and government clients to design continuity programs that are clear, measurable and easy to maintain, with plans your teams actually understand.</p>
    <p>Whether you need a full program or a focused review, we tailor our approach to your needs and deliver outcomes through a trusted team.</p>
  </div>
</section>

<section class="news">
  <div class="news-head">
    <h2>The Latest <span>News</span> &amp; Information</h2>
    <div class="tabs"><a class="on">View all</a><a>Business Continuity</a><a>Disaster Recovery</a><a>Pandemic</a></div>
  </div>
  <div class="news-rule"></div>

  <article class="post" style="left:128px;top:168px;width:330px;height:660px">
    <div class="ph" style="--h:360px;background:linear-gradient(160deg,#c9c3b8,#8d8577)" role="img" aria-label="Photo of a hand using sanitiser at a dispenser"></div>
    <div class="body">
      <h4>COVID19 – Business Recovery Phase</h4>
      <div class="meta">Business Continuity, Pandemic</div>
      <p>The following is a summary of the steps to plan and enter the recovery phase and of addressing new risks that have been identified since the COVID-19 outbreak. We have now entered a new phase, which is the recovery of operations and return to the workplace for many businesses.</p>
    </div>
  </article>

  <article class="post" style="left:479px;top:168px;width:330px;height:190px">
    <div class="body">
      <h4>How's Your User Experience for Your Disaster Recovery?</h4>
      <div class="meta">Disaster Recovery</div>
      <p>It may sound strange to talk about user experience in the context of recovery. After all, the priority is getting systems up and running again within the agreed time.</p>
    </div>
  </article>
  <article class="post" style="left:479px;top:378px;width:330px;height:450px">
    <div class="ph" style="--h:230px;background:linear-gradient(150deg,#9db3c4,#4d6478)" role="img" aria-label="Photo of server racks and network cabling"></div>
    <div class="body">
      <h4>Towards Set-It-And-Forget-It Business Continuity</h4>
      <div class="meta">Business Continuity</div>
      <p>Few activities are as set and forget as we'd wish. Plans age, people move and systems change, so continuity needs a steady, repeatable rhythm of upkeep.</p>
    </div>
  </article>

  <article class="post" style="left:830px;top:168px;width:330px;height:400px">
    <div class="ph" style="--h:180px;background:linear-gradient(140deg,#5e6a74,#2c333a)" role="img" aria-label="Photo of old computer equipment being removed"></div>
    <div class="body">
      <h4>Decommissioning is a Part of Disaster Recovery Planning</h4>
      <div class="meta">Disaster Recovery</div>
      <p>When moving sites or retiring systems, many teams forget the recovery plans that depend on them. Treat decommissioning as a planned change and update your recovery steps.</p>
    </div>
  </article>
  <article class="post" style="left:830px;top:588px;width:330px;height:240px">
    <div class="ph" style="--h:240px;background:linear-gradient(150deg,#d8dadc,#9aa1a8)" role="img" aria-label="Photo of a team meeting in an office"></div>
  </article>

  <span class="btn">View More</span>
</section>

<section class="testi">
  <div class="testi-label"><h2>Our Client<br>Testimonials</h2></div>
  <div class="avatar" role="img" aria-label="Client portrait"></div>
  <div class="quote">"With all due respect, I don't see Brightvale as the classic consultant model. I see you more as hands-on implementers and problem solvers, working closely with us to deliver and implement real solutions to meet our business strategies."
    <b>Dana Morrell – General Manager, Infrastructure Services</b></div>
  <div class="dots"><i class="on"></i><i></i><i></i><i></i></div>
</section>

<footer class="footer">
  <div class="brand"><i></i>Brightvale</div>
  <small>Copyright © 2024 Brightvale</small>
  <div class="footer-links"><span>Privacy</span><span>Disclaimer</span><span>Copyright</span><span>Open Policy</span><span>Social Media</span><span>Sitemap</span></div>
</footer>

</body>
</html>
```